Flyer-Design für medizinische Ausbildung
Zielgruppe
LOTUS Ausbildung für den qualifizierten Krankentransport und Rettungsdienst in Berlin
Der qualifizierte Krankentransport und Rettungsdienst ist zuständig für den Transport- und Versorgung von kranken und verletzten Menschen. LOTUS Medizinische Ausbildung und Seminare hat sich als Fachschule für die präklinische Notfallmedizin auf Aus- und Weiterbildungen für diese zwei Fachbereiche spezialisiert. Unsere Fachausbildungen orientieren sich streng an gesetzlichen Erfordernissen und realitätsnahen medizinischen Anforderungen.
Aufgabenstellung
Bitte farblich an unsere aktuelle Internetseite orientieren. Bilder & Texte können Sie gerne ebenfalls von unserer Website nutzen. www.notfallkurse-zentrum.example

```html
<!DOCTYPE html>
<html lang="de">
<head>
<meta charset="utf-8">
<title>LOTUS Ausbildung – Flyer</title>
<link href="https://fonts.googleapis.com/css2?family=Roboto+Condensed:wght@400;700&family=Source+Sans+3:wght@400;600;700&display=swap" rel="stylesheet">
<style>
  :root{
    --stage:#e8e8e8;
    --paper:#ffffff;
    --brand-blue:#6fa9dc;
    --heading-blue:#5e9fd8;
    --photo-light:#eef1f4;
    --photo-mid:#d9dfe6;
    --photo-warm:#e9d2bf;
    --ink:#2b2b2b;
    --muted:#8a8a8a;
    --white:#ffffff;
  }
  *{margin:0;padding:0;box-sizing:border-box}
  html,body{width:1200px;height:1200px;overflow:hidden;background:var(--stage)}
  body{position:relative;font-family:"Source Sans 3",sans-serif}
  .page{position:absolute;left:215px;width:783px;background:var(--paper);overflow:hidden}
  .page--front{top:35px;height:553px}
  .page--back{top:598px;height:554px}
  .abs{position:absolute}
  .cond{font-family:"Roboto Condensed",sans-serif}
  .headline{font-family:"Roboto Condensed",sans-serif;font-weight:700;font-size:20px;line-height:26px;letter-spacing:.3px;text-transform:uppercase}
  .headline--blue{color:var(--heading-blue)}
  .headline--white{color:var(--white)}
  .body-text{font-size:8.7px;line-height:11.2px;color:var(--white)}

  /* front */
  .front-art{position:absolute;inset:0;width:100%;height:100%}
  .rating-badge{left:38px;top:64px;width:180px;height:180px;border-radius:50%;background:var(--white);border:8px solid #f2f2f2}
  .price-copy{left:27px;top:253px;width:202px;text-align:justify}
  .price-head{left:27px;top:462px}
  .location-map{left:336px;top:249px;width:102px;height:102px;border-radius:50%;background:radial-gradient(circle at 45% 45%,#f4f4f2,#e3e5e6);border:3px solid var(--white)}
  .contact{left:291px;top:352px;width:200px;text-align:center;color:var(--white);font-weight:700}
  .contact p{font-size:10.5px;line-height:21.2px}
  .contact .web{font-size:9px;line-height:15px}
  .contact .web:first-of-type{margin-top:3px}
  .front-brand{right:40px;top:76px;font-family:"Source Sans 3",sans-serif;font-weight:700;font-size:16px;color:var(--white)}
  .mission{left:546px;top:433px}
  .mission .indent{display:block;padding-left:71px}

  /* back */
  .back-photo{left:0;top:0;width:783px;height:196px;background:linear-gradient(115deg,var(--photo-light) 0%,var(--photo-mid) 45%,#cfd5dc 65%,var(--photo-warm) 100%)}
  .for-you{left:27px;top:87px}
  .in-action{right:27px;top:124px}
  .info-band{left:0;top:196px;width:783px;height:308px;background:var(--brand-blue)}
  .icon-ring{width:56px;height:56px;border-radius:50%;border:2px solid var(--white);display:flex;align-items:center;justify-content:center}
  .feature-title{font-size:11px;line-height:13px;font-weight:700;color:var(--white)}
  .feature{color:var(--white)}
  .cta{left:27px;top:428px;width:205px;font-size:10.5px;line-height:12px;font-weight:700;color:var(--white)}
  .cta-note{left:27px;top:463px;width:215px}
  .contact-card{left:280px;top:169px;width:145px;height:104px;background:var(--white);padding:6px 4px 0 4px;color:var(--ink)}
  .contact-card h4{font-family:"Roboto Condensed",sans-serif;font-size:6.6px;font-weight:700;margin-bottom:7px}
  .contact-card p{font-family:"Roboto Condensed",sans-serif;font-size:6.3px;line-height:10px;text-align:justify;width:136px}
  .portrait{left:422px;top:158px;width:124px;height:124px;border-radius:50%;background:var(--white);padding:4px}
  .portrait-fill{width:100%;height:100%;border-radius:50%;border:4px solid var(--brand-blue);background:radial-gradient(circle at 55% 40%,#8a7b70 0%,#5b6470 45%,#b9c4cf 100%)}
  .why-head{left:283px;top:295px;font-size:18px}
  .why-copy{left:283px;top:357px;width:211px;text-align:justify;font-size:8.4px}
  .wordmark{left:360px;top:436px;text-align:center;color:var(--white)}
  .wordmark .name{font-family:"Roboto Condensed",sans-serif;font-weight:700;font-size:40px;line-height:40px;letter-spacing:5px}
  .wordmark .tag{font-family:"Roboto Condensed",sans-serif;font-weight:700;font-size:6.4px;letter-spacing:.3px}
  .overview-head{left:553px;top:206px;font-size:10px;font-weight:700;color:var(--white)}
  .overview-art{left:546px;top:245px;width:218px;height:200px;border-radius:100px;background:radial-gradient(circle,#e6f0fa 0%,#cfe2f4 55%,#a9cbec 100%)}
  .course-list{left:553px;top:454px;list-style:none;font-family:"Roboto Condensed",sans-serif;font-size:10.5px;line-height:14px;color:var(--white)}
  .imprint{left:269px;top:511px;width:240px;font-size:6.6px;line-height:8px;color:var(--muted)}
</style>
</head>
<body>

<section class="page page--front">
  <svg class="front-art" viewBox="0 0 1260 891" preserveAspectRatio="none">
    <rect x="0" y="84" width="1260" height="807" fill="url(#frontPhoto)" role="img" aria-label="Foto: Klemmbrett mit Einsatzprotokoll des Rettungsdienstes"/>
    <defs>
      <linearGradient id="frontPhoto" x1="0" y1="0" x2="1" y2="1">
        <stop offset="0" stop-color="#e9edf2"/>
        <stop offset=".5" stop-color="#f3f4f5"/>
        <stop offset="1" stop-color="#e4e8ee"/>
      </linearGradient>
    </defs>
    <polygon points="0,168 330,84 400,84 360,351 1260,728 1260,891 795,891 0,535" fill="var(--brand-blue)"/>
    <polygon points="0,535 795,891 0,891" fill="#f5f6f7"/>
    <rect x="0" y="0" width="1260" height="84" fill="var(--paper)"/>
  </svg>

  <div class="abs rating-badge" role="img" aria-label="Bewertungssiegel"></div>

  <p class="abs body-text price-copy">Immer wieder wird gefragt, weshalb die Preise bei LOTUS so moderat sind. Die Antwort ist kurz und knapp beantwortet, wir möchten unsere Ausbildungen Jedem ermöglichen. Speziell die Zielgruppe, die keine Förderungen durch die Arbeitsagenturen in Anspruch nehmen können. Unsere Branche benötigt dringend Nachwuchs. Aufgrund dessen fördern wir auf unsere Art mit fairen Preisen zukünftiges, motiviertes und junges Fachpersonal.</p>

  <h2 class="abs headline headline--blue price-head">Unsere unsere<br>Preise sind fair und<br>sozial.</h2>

  <div class="abs location-map" role="img" aria-label="Kartenausschnitt mit Standort der Schule"></div>

  <div class="abs contact">
    <p>Lindenweg 12</p>
    <p>10115 Berlin</p>
    <p>Tel. + 030 1234567 30</p>
    <p>Fax +030 1234567 31</p>
    <p class="web">info@notfallkurse-zentrum.example</p>
    <p class="web">www.notfallkurse-zentrum.example</p>
  </div>

  <div class="abs front-brand">LOTUS</div>

  <h2 class="abs headline headline--white mission">Wir sind<br>für Sie ...<br><span class="indent">... im Einsatz</span></h2>
</section>

<section class="page page--back">
  <div class="abs back-photo" role="img" aria-label="Foto: Klemmbrett mit Einsatzprotokoll für den qualifizierten Krankentransport"></div>
  <h2 class="abs headline headline--blue for-you">Für Sie ...</h2>
  <h2 class="abs headline headline--blue in-action">... im Einsatz</h2>

  <div class="abs info-band"></div>

  <div class="abs icon-ring" style="left:28px;top:208px">
    <svg width="30" height="30" viewBox="0 0 30 30" fill="none" stroke="#fff" stroke-width="1.4" stroke-linecap="round" stroke-linejoin="round">
      <rect x="3" y="5" width="24" height="16" rx="1.5"/><path d="M11 26h8M15 21v5"/><path d="M15 8c2 2 2.5 5 1.5 8h-3c-1-3-.5-6 1.5-8z"/><path d="M13.5 16l-2 2M16.5 16l2 2"/>
    </svg>
  </div>
  <div class="abs feature" style="left:94px;top:205px;width:135px">
    <div class="feature-title">Qualifizierte Fachschule</div>
    <p class="body-text">Fachausbildungen streng nach­gesetzlichen Erfordernissen und realitätsnahen medizinischen Anforderungen.</p>
  </div>

  <div class="abs feature" style="left:27px;top:277px;width:140px">
    <div class="feature-title">Medizinische Ausbildung-</div>
    <p class="body-text">LOTUS hat sich als Fachschule für die präklinische Notfallmedizin auf Aus- und Weiterbildungen für diese zwei Fachbereiche spezialisiert.</p>
  </div>
  <div class="abs icon-ring" style="left:172px;top:284px">
    <svg width="30" height="30" viewBox="0 0 30 30" fill="none" stroke="#fff" stroke-width="1.4" stroke-linecap="round" stroke-linejoin="round">
      <rect x="4" y="4" width="22" height="20" rx="1.5"/><path d="M4 9h22"/><path d="M11 25v-8h3l2-5c1.5 0 2 1 1.5 3h4c1 0 1.5 1 1 2l-1.5 6c-.3 1-1 1.5-2 1.5H11z"/>
    </svg>
  </div>

  <div class="abs icon-ring" style="left:28px;top:355px">
    <svg width="30" height="30" viewBox="0 0 30 30" fill="none" stroke="#fff" stroke-width="1.4" stroke-linecap="round" stroke-linejoin="round">
      <path d="M8 4h13v20H8z"/><path d="M11 9h7M11 12h7M11 15h4"/><circle cx="11" cy="21" r="5"/><path d="M13 19h-3M13 22h-3M12.5 18.5c-1-.5-2.5 0-2.5 2.5s1.5 3 2.5 2.5"/><path d="M21 26v-6M24 26v-9"/>
    </svg>
  </div>
  <div class="abs feature" style="left:94px;top:350px;width:140px">
    <div class="feature-title">Faire Preise</div>
    <p class="body-text">Unsere Branche benötigt dringend Nachwuchs. Aufgrund dessen fördern wir auf unsere Art mit fairen Preisen zukünftiges, motiviertes und junges Fachpersonal.</p>
  </div>

  <p class="abs cta">Jetzt Ausbildungplatz zum fairen Preis sichern!</p>
  <p class="abs body-text cta-note">Näherer Informationen in unsrere Website oder rufen Sie uns an, wir helfen Ihnen gerne weiter.</p>

  <div class="abs contact-card">
    <h4>Ihr Ansprechpartner bei LOTUS</h4>
    <p>Markus Lohmann ist Rettungsfachkraft aus Leidenschaft und Schulleiter von LOTUS Medizinische Ausbildung u. Seminare. Als Fachausbilder für den qualifizierten Krankentransport ist er Dozent, Mentor und Ansprechpartner, auch nach Abschluss der Ausbildung. Ganz nach dem Motto: „Entweder finden wir einen Weg oder wir machen einen.“</p>
  </div>
  <div class="abs portrait"><div class="portrait-fill" role="img" aria-label="Porträtfoto des Ansprechpartners"></div></div>

  <h2 class="abs headline headline--white why-head">Warum eine<br>Ausbildung bei LOTUS?</h2>
  <p class="abs body-text why-copy">Wir bieten Ihnen eine umfassende Fachausbildung in Form von handlungs- und lernorientiertem Unterricht. Unsere Lehrbeauftragten sind erfahrende Rettungsdienstler, Pflegekräfte und Mediziner mit weitreichender Berufserfahrung. Durch fundierte Fachinhalte, praxisrelevanter Methodik und geschulter Didaktik beschulen und begleiten wir Sie bis zum gewünschten Fachabschluss.</p>

  <div class="abs wordmark">
    <div class="name">LOTUS</div>
    <div class="tag">Medizinische Ausbildung u. Seminare</div>
  </div>

  <h3 class="abs overview-head">Unsere Ausbildungen im Überblick:</h3>
  <div class="abs overview-art" role="img" aria-label="Illustration: Ausbildungsbereiche mit Rettungswagen, Patientenversorgung und Teamarbeit"></div>
  <ul class="abs course-list">
    <li>- Ausbildung zum Transportsanitäter</li>
    <li>- Ausbildung zum Rettungshelfer</li>
    <li>- Ausbildung zum Rettungssanitäter</li>
  </ul>

  <p class="abs imprint">LOTUS Medizinische Ausbildung und Seminare<br>Fachschule für den qualifizierten Krankentransport und Rettungsdienst in Berlin</p>
</section>

</body>
</html>
```